Microblading website contest - Make it colorful

Beauty salon focusing on microblading need a better website template. Please make a 1 page site mobile optimized and nicer layout with better color formulation. Would love interactive images in the site. You can use stock images and if approve we can pay for it.
Current site:
tessawynkelpeony.com

Inspiration:
https://framqueue.net/shots/41877260-Microblading-HomePage
https://framqueue.net/shots/7914026-Lunetto-Microblading-Eyebrow-Beauty-Salon-Pagewright-Theme

Target Market(s)

women

Industry/Entity Type

beauty salon

Number of Pages Required

1 page

Font styles to use
Serif
Decorative
Script

Requirements
Nice to have
• As pretty as possible

```html
<!DOCTYPE html>
<html lang="en">
<head>
<meta charset="utf-8">
<title>Studio Arch Tessa – Microblading</title>
<link href="https://fonts.googleapis.com/css2?family=Federo&family=Poppins:wght@300;400;500&display=swap" rel="stylesheet">
<style>
:root{
  --pink:#dc4d76;
  --pink-soft:#e7788f;
  --pink-deep:#d8346c;
  --ink:#1a1a1a;
  --grey:#555;
  --line:#9a9a9a;
  --cream:#f7f3ee;
  --white:#fff;
  --black:#000;
}
*{margin:0;padding:0;box-sizing:border-box}
html,body{width:1200px;height:4381px;overflow:hidden}
body{position:relative;background:var(--white);font-family:'Poppins',sans-serif;color:var(--ink)}
.abs{position:absolute}
.deco{font-family:'Federo',sans-serif}
.btn{position:absolute;display:flex;align-items:center;justify-content:center;font-size:12px;border-radius:6px;color:var(--white);background:linear-gradient(90deg,var(--pink-soft),var(--pink))}
.btn-outline{background:var(--white);color:var(--pink);border:1px solid var(--pink)}
.photo{position:absolute}

/* header */
.logo-dot{left:170px;top:32px;width:22px;height:22px;border-radius:50%;background:var(--pink)}
.logo-name{left:204px;top:30px;font-size:18px;line-height:20px;letter-spacing:1px;color:#222}
.nav{top:32px;font-size:13px;color:#222}
.book{left:937px;top:24px;width:98px;height:32px}
.burger{left:1054px;top:32px;width:21px;height:16px}

/* hero */
.hero{left:0;top:0;width:1200px;height:643px;background:linear-gradient(90deg,var(--cream) 0%,#f6ece6 22%,#e7c7a8 38%,#d8b08c 55%,#c98f7a 70%,#ecc9b6 100%)}
.hero-title{left:204px;top:150px;font-size:56px;line-height:62px;color:var(--pink);letter-spacing:2px}
.hero-sub{left:206px;top:288px;font-size:16px}
.hero-btn{left:206px;top:365px;width:102px;height:31px}

/* about */
.welcome{left:206px;top:738px;font-size:11px;font-weight:500}
.welcome-name{left:302px;top:722px;font-size:32px;color:var(--pink)}
.about-band{left:0;top:796px;width:1200px;height:445px;background:linear-gradient(180deg,var(--pink-soft),var(--pink-deep))}
.portrait{left:206px;top:772px;width:386px;height:495px;background:linear-gradient(180deg,#bdbdbd,#d6d4d2 60%,#c9c6c3)}
.bio{left:639px;top:834px;width:360px;font-size:11px;line-height:17px;color:var(--white);font-weight:300}
.bio p{margin-bottom:12px}

/* microblading */
.leaf{top:1380px;width:170px;height:320px;background:radial-gradient(ellipse,#eeeeee,#fff 70%)}
.micro-photo{left:206px;top:1367px;width:789px;height:342px;background:linear-gradient(120deg,#3a3430,#d9d4cf 45%,#f1ece6 60%,#2a2623)}
.micro-title{left:206px;top:1749px;font-size:16px;font-weight:500}
.micro-text{left:206px;top:1772px;width:790px;font-size:11px;line-height:17px;color:#333}
.micro-btn{left:206px;top:1860px;width:89px;height:33px}

/* gallery */
.gal-title{left:128px;top:2010px;font-size:56px;letter-spacing:2px}
.gal-sub{left:133px;top:2078px;font-size:16px;color:var(--pink);letter-spacing:1px}
.gal-line{left:340px;top:2088px;width:660px;height:1px;background:var(--line)}
.gal-brow{left:1004px;top:2076px;width:72px;height:14px;background:linear-gradient(90deg,#bbb,#555);border-radius:50% 50% 0 0}
.g{position:absolute;border:1px solid #fff}
.show-more{left:297px;top:2734px;width:97px;height:34px}

/* stats */
.stats{left:0;top:2851px;width:1200px;height:149px;background:linear-gradient(180deg,var(--pink-soft),var(--pink-deep))}
.stat{position:absolute;top:2892px;width:200px;text-align:center;color:var(--white)}
.stat b{display:block;font-weight:400;font-size:32px;line-height:38px}
.stat span{font-size:13px}

/* beauty */
.beauty-title{left:0;top:3048px;width:1200px;text-align:center;font-size:60px;letter-spacing:2px}
.beauty-sub{left:0;top:3136px;width:1200px;text-align:center;font-size:15px;color:var(--pink);letter-spacing:1px}
.card{position:absolute;width:249px;height:197px;background:linear-gradient(180deg,var(--pink-soft),var(--pink-deep));box-shadow:0 3px 8px rgba(0,0,0,.2);color:var(--white);text-align:center;padding:20px 8px}
.card h3{font-family:'Federo',sans-serif;font-weight:400;font-size:18px;line-height:28px;letter-spacing:.5px;margin-bottom:18px;white-space:nowrap}
.card p{font-size:12px;line-height:20px;padding:0 8px}
.beauty-more{left:551px;top:3437px;width:98px;height:33px}

/* services */
.svc-title{left:0;top:3500px;width:1200px;text-align:center;font-size:54px;color:var(--pink);letter-spacing:2px}
.svc-text{left:0;top:3576px;width:1200px;text-align:center;font-size:15px;line-height:25px}
.svc{position:absolute;width:297px;height:255px;border:1px solid #e6e6e6;box-shadow:0 2px 6px rgba(0,0,0,.08);background:var(--white);text-align:center;padding:24px 16px;font-size:13px;line-height:20px}
.svc svg{display:block;margin:0 auto 10px}
.svc h4{font-weight:400;color:var(--pink);font-size:16px;line-height:24px;margin-bottom:8px}
.svc p{margin-bottom:12px}
.svc-more{left:541px;top:4026px;width:117px;height:30px}

/* footer */
.footer{left:0;top:4153px;width:1200px;height:228px;background:var(--black)}
.cta{left:128px;top:4131px;width:943px;height:117px;background:linear-gradient(90deg,#e05a80,#de4d76 60%,#e78aa0)}
.cta-text{left:156px;top:4158px;font-size:30px;line-height:38px;color:var(--white);letter-spacing:1.5px}
.cta-btn{left:882px;top:4168px;width:157px;height:41px;border:1px solid var(--white);border-radius:21px;color:var(--white);font-size:17px;display:flex;align-items:center;justify-content:center}
.addr{right:129px;top:4276px;text-align:right;font-size:12px;line-height:20px;color:var(--white)}
.copy{left:126px;top:4342px;font-size:10px;color:var(--white)}
.legal{right:129px;top:4342px;font-size:10px;color:var(--white)}
</style>
</head>
<body>

<!-- Hero -->
<div class="photo hero" role="img" aria-label="Makeup artist applying eye makeup to a client"></div>
<div class="abs logo-dot"></div>
<div class="abs logo-name deco">STUDIO ARCH<br>TESSA</div>
<div class="abs nav" style="left:454px">Home</div>
<div class="abs nav" style="left:519px">About me</div>
<div class="abs nav" style="left:607px">My services</div>
<div class="abs nav" style="left:705px">Gallery</div>
<div class="abs nav" style="left:779px">Shop</div>
<div class="btn book">BOOK NOW</div>
<svg class="abs burger" viewBox="0 0 21 16"><rect y="0" width="21" height="2.5" fill="#111"/><rect y="6.5" width="21" height="2.5" fill="#111"/><rect y="13" width="21" height="2.5" fill="#111"/></svg>
<h1 class="abs hero-title deco" style="font-weight:400">STUDIO OF<br>ARCH TESSA</h1>
<div class="abs hero-sub">Your personal eyebrow specialist</div>
<div class="btn hero-btn">Contact Me</div>

<!-- About -->
<div class="abs welcome">WELCOME TO</div>
<div class="abs welcome-name deco">TESSA</div>
<div class="abs about-band"></div>
<div class="photo portrait" role="img" aria-label="Portrait of Tessa, eyebrow specialist"></div>
<div class="abs bio">
  <p>Tessa has 7 years of microblading experience. She graduated from VelaTouch United States. After, she studied in Arcademy, a global top brand from Germany. She was personally guided by the brand CEO Dario Kovenic and the first China Master Mei Lan.</p>
  <p>After earning award of ArcBrows Artist in 2019, Tessa continued her practice microblading until she won the world's first ArcBrows Master in Taiwan in 2021. She is currently the only certificated Master technician in Taiwan. She also holds a shading and ArcBright Master.</p>
  <p>On Tessa's microblading journey, She travelled to places all over the world and met mentors on her path. She was willing to learn any new tech and inspire a better self regardless how much the cost was.</p>
  <p>Today, Tessa has become one of the very successful eyebrow tattoo artists in New York. No matter what the eyebrow trend is, Tessa focuses on how to provide an exclusive and the most suitable eyebrow for each clients.</p>
</div>

<!-- Microblading -->
<div class="photo leaf" style="left:38px" role="img" aria-label="Line-art leaf decoration"></div>
<div class="photo leaf" style="left:995px" role="img" aria-label="Line-art leaf decoration"></div>
<div class="photo micro-photo" role="img" aria-label="Artist performing microblading on a client"></div>
<div class="abs micro-title">Microblading</div>
<div class="abs micro-text">Microblading is a semi-permanent makeup. I will create strokes of pigment under the skin that resemble hair to give a natural full eyebrow effect. I specialize in the feathering technique to give a natural everyday brow. Whether you are getting out of the shower, swimming or working out, you won't have to worry about your eyebrows.</div>
<div class="btn micro-btn">See More</div>

<!-- Gallery -->
<h2 class="abs gal-title deco" style="font-weight:400">GALLERY</h2>
<div class="abs gal-sub">CHECK OUT MY WORK!</div>
<div class="abs gal-line"></div>
<div class="photo gal-brow" role="img" aria-label="Eyebrow illustration"></div>
<div class="g" style="left:204px;top:2138px;width:219px;height:278px;background:linear-gradient(160deg,#c9c8c4,#7d838a)" role="img" aria-label="Training class photo"></div>
<div class="g" style="left:250px;top:2184px;width:219px;height:278px;background:linear-gradient(160deg,#d8d6d2,#5f646b)" role="img" aria-label="Training class photo"></div>
<div class="g" style="left:297px;top:2230px;width:218px;height:279px;background:linear-gradient(160deg,#e6e2dc,#b7aa98 50%,#3a3835)" role="img" aria-label="Students practicing brow drawing"></div>
<div class="g" style="left:535px;top:2230px;width:218px;height:279px;background:linear-gradient(180deg,#c9a03a,#2d2b29 55%,#c8c2b8)" role="img" aria-label="Graduates with certificates and balloons"></div>
<div class="g" style="left:775px;top:2230px;width:218px;height:279px;background:linear-gradient(180deg,#e8e6e2,#c9c6c1 55%,#8c7f75)" role="img" aria-label="Instructor presenting in a classroom"></div>
<div class="g" style="left:297px;top:2529px;width:218px;height:169px;background:linear-gradient(160deg,#dfe3e6,#5a5f66)" role="img" aria-label="Microblading treatment in progress"></div>
<div class="g" style="left:535px;top:2529px;width:218px;height:169px;background:linear-gradient(160deg,#ece9e5,#8a8580)" role="img" aria-label="Students practicing on models"></div>
<div class="g" style="left:775px;top:2529px;width:218px;height:169px;background:linear-gradient(160deg,#e4e6e9,#6e7378)" role="img" aria-label="Artist working on a client's brows"></div>
<div class="btn btn-outline show-more">Show More</div>

<!-- Stats -->
<div class="abs stats"></div>
<div class="stat" style="left:238px"><b>1000+</b><span>Happy Clients</span></div>
<div class="stat" style="left:497px"><b>5+</b><span>Years of Experience</span></div>
<div class="stat" style="left:769px"><b>5</b><span>Star Ratings</span></div>

<!-- Beauty -->
<h2 class="abs beauty-title deco" style="font-weight:400">YOUR EYEBROWS AND BEAUTY</h2>
<div class="abs beauty-sub">LET US TAKE CARE OF IT</div>
<div class="card" style="left:204px;top:3167px"><h3>LICENSED<br>MICROBLADING ARTIST</h3><p>LICENSE FROM VARIOUS STATES<br>IN UNITED STATE</p></div>
<div class="card" style="left:476px;top:3199px"><h3>YEARS OF<br>EXPERIENCE</h3><p>OVER THOUSANDS OF CASES<br>OVERSEA STUDY AND PRACTICE</p></div>
<div class="card" style="left:746px;top:3167px"><h3>EUROPEAN LATEST<br>TECHNIQUE</h3><p>WE STUDY EUROPEAN-STYLE NATURAL HAIR FLOW, IMPROVE AND MAKE IT SUITABLE FOR ASIANS</p></div>
<div class="btn btn-outline beauty-more">Show More</div>

<!-- Services -->
<h2 class="abs svc-title deco" style="font-weight:400">SPECIALIZED SERVICE</h2>
<div class="abs svc-text">WE TREAT EVERY CLIENT AS OUR FRIENDS AND FAMILY. WE GIVE YOU THE MOST SINCERE<br>ADVISE AND BEST QUALITY AND SERVICE.<br><span style="display:inline-block;margin-top:8px">WE DO NOT ONLY FOLLOW THE TREND. WE HEAR YOU, AND WANT YOU TO LOVE IT FOREVER.</span></div>

<div class="svc" style="left:124px;top:3762px">
  <svg width="40" height="40" viewBox="0 0 40 40" fill="none" stroke="#333" stroke-width="1.3"><circle cx="20" cy="20" r="7"/><circle cx="20" cy="20" r="3"/><path d="M20 3v6M20 31v6M3 20h6M31 20h6M8 8l4 4M28 28l4 4M32 8l-4 4M12 28l-4 4"/></svg>
  <h4>NATURAL BROWS</h4><p>Microblading | Hand-drawing<br>hair lines</p><p>For all skin type</p>
</div>
<div class="svc" style="left:451px;top:3728px">
  <svg width="40" height="40" viewBox="0 0 40 40" fill="none" stroke="#333" stroke-width="1.3"><circle cx="20" cy="20" r="7"/><circle cx="20" cy="20" r="3"/><path d="M20 3v6M20 31v6M3 20h6M31 20h6M8 8l4 4M28 28l4 4M32 8l-4 4M12 28l-4 4"/></svg>
  <h4>POWDER EYELINER<br>(NATURAL EYESHADOW)</h4><p>Extend eyeline at end of the eye|#<br>With a touch of ligh eyeshadow vision</p><p>For those who like to have<br>an eye makeup filter<br>24/7 | Eye-shape adjustment</p>
</div>
<div class="svc" style="left:779px;top:3762px">
  <svg width="40" height="40" viewBox="0 0 40 40" fill="none" stroke="#333" stroke-width="1.3"><circle cx="20" cy="20" r="7"/><circle cx="20" cy="20" r="3"/><path d="M20 3v6M20 31v6M3 20h6M31 20h6M8 8l4 4M28 28l4 4M32 8l-4 4M12 28l-4 4"/></svg>
  <h4>SCALP MICROPIGMENTATION</h4><p>Add destiny to the thinning<br>area | Seamless and Undetectable | Accommodates your skin tone and natural hair color | providing the appearance of hair</p><p>For restoring hairline | Bald spots | Scar covering</p>
</div>
<div class="btn svc-more">More Services</div>

<!-- Footer -->
<div class="abs footer"></div>
<div class="photo cta" role="img" aria-label="Pink banner over a brow treatment photo"></div>
<div class="abs cta-text deco">GREAT BROWS DON'T HAPPEN BY CHANCE,<br>THEY HAPPEN BY APPOINTMENT</div>
<div class="abs cta-btn">Contact US</div>
<div class="abs addr">2740 Orchard Ave #118, Brookvale, NY<br>10457 Studio Arch Tessa Inc</div>
<div class="abs copy">© 2023 Welcome. All right reserved.</div>
<div class="abs legal">Privacy Policy &nbsp;/ Terms of Service</div>

</body>
</html>
```